Borealis Film and Design
Your Moments on Reels
Borealis Film and Design -
Creative Brief
Professional
Peter Vandrell
2187 Kettering Ln. North Pole, Alaska 99612
Peter@borealisfilmanddesign.example
borealisfilmanddesign.example

```html
<!DOCTYPE html>
<html lang="en">
<head>
<meta charset="UTF-8">
<title>Borealis Film and Design – Business Card</title>
<link rel="stylesheet" href="https://fonts.googleapis.com/css2?family=Arimo:wght@400;700&display=swap">
<style>
  :root {
    --backdrop: #e9e6e2;
    --card: #ffffff;
    --navy: #1f2a6b;
    --royal: #3340a8;
    --band-deep: #1c2480;
    --ink: #111111;
    --text-grey: #5a5a5a;
    --rule: #b5b5b5;
  }
  * { margin: 0; padding: 0; box-sizing: border-box; }
  html, body {
    width: 1200px;
    height: 780px;
    overflow: hidden;
    background: var(--backdrop);
    font-family: "Arimo", Arial, sans-serif;
  }
  .card {
    position: absolute;
    left: 80px;
    top: 90px;
    width: 1040px;
    height: 600px;
    background: var(--card);
    border-radius: 34px;
    overflow: hidden;
    box-shadow: 0 6px 24px rgba(0,0,0,0.18);
  }
  .card-swoosh {
    position: absolute;
    left: 0;
    bottom: 0;
    width: 100%;
    height: 260px;
  }
  .brand {
    position: absolute;
    top: 140px;
    left: 0;
    width: 100%;
    display: flex;
    justify-content: center;
    align-items: center;
    gap: 22px;
  }
  .brand-dot {
    width: 64px;
    height: 64px;
    border-radius: 50%;
    background: var(--royal);
  }
  .brand-name {
    font-size: 54px;
    font-weight: 700;
    color: var(--navy);
    letter-spacing: 1px;
  }
  .holder {
    position: absolute;
    top: 320px;
    right: 600px;
    text-align: right;
  }
  .holder-name {
    font-size: 26px;
    font-weight: 700;
    color: var(--royal);
    margin-bottom: 30px;
  }
  .holder-address {
    font-size: 21px;
    line-height: 31px;
    color: var(--text-grey);
  }
  .divider {
    position: absolute;
    left: 462px;
    top: 292px;
    width: 2px;
    height: 150px;
    background: var(--rule);
  }
  .contact {
    position: absolute;
    left: 480px;
    top: 288px;
    list-style: none;
  }
  .contact li {
    display: flex;
    align-items: center;
    gap: 10px;
    height: 32px;
    font-size: 20px;
    color: var(--text-grey);
  }
  .contact-icon {
    width: 20px;
    height: 20px;
    flex: none;
  }
  .contact-icon--blank { visibility: hidden; }
</style>
</head>
<body>
  <div class="card">
    <svg class="card-swoosh" viewBox="0 0 1040 260" preserveAspectRatio="none" aria-hidden="true">
      <defs>
        <linearGradient id="bandFill" x1="0" y1="0" x2="1" y2="0">
          <stop offset="0" stop-color="#3f4cc0"/>
          <stop offset="1" stop-color="#1c2480"/>
        </linearGradient>
      </defs>
      <path d="M0 225 C 320 215, 700 180, 1040 60 L1040 260 L0 260 Z" fill="url(#bandFill)"/>
      <path d="M0 205 C 330 200, 700 165, 1040 40 L1040 62 C 700 190, 320 218, 0 226 Z" fill="#ffffff"/>
      <path d="M0 195 C 330 190, 690 150, 1040 22 L1040 40 C 700 165, 330 200, 0 205 Z" fill="#111111"/>
    </svg>

    <div class="brand">
      <span class="brand-dot"></span>
      <span class="brand-name">Borealis Film and Design</span>
    </div>

    <div class="holder">
      <p class="holder-name">Peter Vandrell</p>
      <p class="holder-address">2187 Kettering Ln.<br>North Pole, Alaska 99612</p>
    </div>

    <div class="divider"></div>

    <ul class="contact">
      <li>
        <svg class="contact-icon" viewBox="0 0 20 20" aria-hidden="true">
          <rect x="5" y="1" width="10" height="18" rx="2" fill="none" stroke="#1f2a6b" stroke-width="2"/>
          <rect x="7" y="4" width="6" height="8" fill="#3340a8"/>
        </svg>
        1-907-555-0182
      </li>
      <li>
        <svg class="contact-icon" viewBox="0 0 20 20" aria-hidden="true">
          <text x="10" y="16" text-anchor="middle" font-size="18" font-weight="700" fill="#1f2a6b" font-family="Arimo, sans-serif">@</text>
        </svg>
        Peter@borealisfilmanddesign.example
      </li>
      <li>
        <svg class="contact-icon" viewBox="0 0 20 20" aria-hidden="true">
          <circle cx="10" cy="10" r="8" fill="#7a86d6"/>
          <path d="M2 10 H18 M10 2 C6 6,6 14,10 18 M10 2 C14 6,14 14,10 18" stroke="#ffffff" stroke-width="1.2" fill="none"/>
        </svg>
        borealisfilmanddesign.example
      </li>
      <li>
        <span class="contact-icon contact-icon--blank"></span>
        License No : 418306
      </li>
    </ul>
  </div>
</body>
</html>
```